Create a Dynamic Website for Roadhaven 41Ter!

Dear designers,
We have an exciting design opportunity for you on Pixelmoot. We are in need of a creative and professional website design for our company, Roadhaven 41Ter. Our current website is outdated and fails to convey the image we want to project. We are determined to revamp our online presence and create a website that truly represents who we are.
Roadhaven 41Ter is a versatile establishment offering a Kelmo Mart, sandwich bar, restaurant, parking facilities, and meeting rooms. Each of these aspects deserves its own spotlight on our website. Therefore, we are seeking a WordPress-based website design that allows us to easily make changes, modify texts, and add new content as needed.
It is crucial that the design aligns seamlessly with our new branding and style. We invite you to explore our Instagram (@Roadhaven41ter) and Facebook (@Roadhaven) pages to gain an understanding of our branding and incorporate those elements into the design.
You can find our current website at www.calmroadhaven.eu, but we want a new website that is vibrant, dynamic, and includes moving elements if possible. We believe this will enhance the user experience and keep visitors engaged for longer periods.
Key elements we would like to include in the new website design are as follows:
Clear presentation of all our services: Kelmo Mart, sandwich bar, restaurant, parking facilities, and meeting rooms.
Easy navigation for visitors to find information effortlessly.
Engaging call-to-action buttons that encourage visitors to take specific actions, such as reserving a meeting room or placing an order.
A dedicated blog section where we can share news, events, and special offers.
Integration of a contact form and contact details for easy communication with our visitors.
Responsive design that works seamlessly across desktop and mobile devices.
We envision a modern and visually appealing website that leaves a lasting positive impression on visitors. We are interested in a design that incorporates creative visual elements and provides a user-friendly interface.
Thank you for your time, and we eagerly await your designs.
Best regards,

```html
<!DOCTYPE html>
<html lang="nl">
<head>
<meta charset="utf-8">
<title>Roadhaven 41Ter</title>
<link href="https://fonts.googleapis.com/css2?family=Oswald:wght@400;500;600&family=Poppins:wght@400;500;600&display=swap" rel="stylesheet">
<style>
:root{
  --red:#d31f26;
  --blue:#1f73c1;
  --navy:#24235a;
  --ink:#1d1d1f;
  --muted:#8a8a8a;
  --grey:#f2f2f2;
  --line:#e4e4e4;
}
*{box-sizing:border-box;margin:0;padding:0}
html,body{width:1200px;height:5376px;overflow:hidden;background:#fff}
body{font-family:"Poppins",sans-serif;color:var(--ink);position:relative}
.section{position:absolute;left:0;width:1200px;overflow:hidden}
.abs{position:absolute}
.head{font-family:"Oswald",sans-serif;font-weight:500;text-transform:uppercase;letter-spacing:.3px}
.accent{color:var(--blue)}
.btn{position:absolute;display:flex;align-items:center;justify-content:center;background:var(--red);color:#fff;font-family:"Oswald",sans-serif;font-weight:500;font-size:14px;border-radius:5px}
.btn-outline{background:#fff;color:var(--red);border:2px solid var(--red)}
.photo{position:absolute}

/* header */
.site-header{top:0;height:108px}
.brand{left:100px;top:26px;width:160px;height:60px;display:flex;align-items:center;font-family:"Oswald",sans-serif;font-weight:600;font-size:22px;color:var(--navy);line-height:1.05}
.nav{left:305px;top:44px;display:flex;gap:26px;font-size:13px;color:#333}

/* hero */
.hero{top:108px;height:637px;background:radial-gradient(circle at 75% 35%,#8a5a3a 0%,#4a3326 40%,#2a211c 100%)}
.hero-kicker{left:98px;top:152px;color:#fff;font-size:34px}
.hero-title{left:98px;top:200px;color:#fff;font-size:58px;font-weight:600}

/* hours */
.hours{top:745px;height:705px}
.hours-title{left:98px;top:105px;font-size:30px;color:var(--navy)}
.hours-table{left:98px;top:170px;width:330px}
.hours-row{display:flex;justify-content:space-between;align-items:center;height:52px;border-bottom:1px solid var(--line)}
.hours-row .day{font-family:"Oswald",sans-serif;font-size:20px}
.hours-row .time{font-size:14px}
.hours-note{left:98px;top:555px;font-family:"Oswald",sans-serif;color:var(--red);font-size:16px}

/* about band */
.about{top:1450px;height:526px;background:var(--navy)}
.about-text{left:608px;top:140px;width:495px;color:#fff;font-size:12.4px;line-height:23px}

/* meetings */
.meet{top:1976px;height:497px;text-align:center}
.center-title{left:0;width:1200px;text-align:center;font-size:32px;color:var(--navy)}
.meet-text{left:170px;width:860px;top:178px;font-size:15px;line-height:27px}

/* services */
.services{top:2473px;height:424px}
.service{position:absolute;top:144px;width:200px;text-align:center;font-size:16px}
.service .ring{width:130px;height:130px;border-radius:50%;border:7px solid var(--blue);margin:0 auto 24px}

/* restaurant */
.resto{top:2897px;height:766px;background:var(--grey)}
.small-copy{font-size:10.5px;line-height:21px;color:#333}

/* blog */
.blog{top:3663px;height:709px}
.post{position:absolute;top:197px;width:325px}
.post .img{height:200px}
.post .date{position:absolute;left:32px;top:185px;background:var(--blue);color:#fff;font-size:12px;padding:9px 16px}
.post h3{font-weight:500;font-size:19px;line-height:29px;margin-top:50px}
.post p{font-size:14px;line-height:26px;color:var(--muted);margin-top:8px}
.post .more{font-size:13px;font-weight:600;color:var(--red);margin-top:14px}

/* contact */
.contact{top:4372px;height:547px;background:var(--blue)}
.field{position:absolute;background:#fff;height:50px;border-radius:3px;display:flex;align-items:center;justify-content:space-between;padding:0 22px;font-size:14px;color:#666}

/* footer */
.footer{top:4919px;height:457px}
.foot-title{font-weight:600;font-size:20px}
.foot-list{font-size:13px;line-height:23px;color:#333;margin-top:20px}
.icon-dot{width:40px;height:40px;border-radius:50%;background:var(--navy);display:flex;align-items:center;justify-content:center}
.contact-item{position:absolute;left:472px;display:flex;gap:20px;font-size:13px;line-height:22px}
</style>
</head>
<body>

<header class="section site-header">
  <div class="abs brand">ROADHAVEN 41TER</div>
  <nav class="abs nav"><span>Home</span><span>Over Ons</span><span>Broodjesbar</span><span>Restaurant</span><span>Parking</span><span>Kelmo Mart</span><span>Contact</span></nav>
  <div class="btn" style="left:928px;top:30px;width:174px;height:50px">Een Bestelling Plaatsen</div>
</header>

<section class="section hero" role="img" aria-label="Friends raising glasses of wine and spritz outdoors with warm bokeh lights">
  <div class="abs head hero-kicker">Welkom bij</div>
  <div class="abs head hero-title">Calm Roadhaven</div>
  <div class="btn" style="left:98px;top:307px;width:114px;height:53px">Begin</div>
</section>

<section class="section hours">
  <h2 class="abs head hours-title">Kelmo <span class="accent">Mart</span></h2>
  <div class="abs hours-table">
    <div class="hours-row"><span class="day">Maandag</span><span class="time">05:30–22:00</span></div>
    <div class="hours-row"><span class="day">Dinsdag</span><span class="time">05:30–22:00</span></div>
    <div class="hours-row"><span class="day">Woensdag</span><span class="time">05:30–22:00</span></div>
    <div class="hours-row"><span class="day">Donderdag</span><span class="time">05:30–22:00</span></div>
    <div class="hours-row"><span class="day">Vrijdag</span><span class="time">05:30–22:00</span></div>
    <div class="hours-row"><span class="day">Zaterdag</span><span class="time">08:00–22:00</span></div>
    <div class="hours-row" style="border:0"><span class="day">Zondag</span><span class="time">08:00–22:00</span></div>
  </div>
  <div class="abs hours-note">Restaurant van 08u</div>
  <div class="abs" style="left:608px;top:155px;width:454px;height:440px;background:var(--blue)"></div>
  <div class="photo" role="img" aria-label="Smiling bar employee in a blue shirt behind the counter" style="left:588px;top:135px;width:452px;height:435px;background:linear-gradient(160deg,#c9a877,#7fa6b8 55%,#3e5b6e)"></div>
</section>

<section class="section about">
  <div class="photo" role="img" aria-label="Glazed grilled ribs with a fresh salad bowl" style="left:0;top:0;width:620px;height:526px;background:linear-gradient(90deg,#5a2a16 0%,#7a3a1c 45%,#3a2a3a 80%,var(--navy) 100%)"></div>
  <h2 class="abs head" style="left:608px;top:70px;color:#fff;font-size:30px">Zoveel meer dan een truckstop.</h2>
  <p class="abs about-text">In 2009 ontstond Roadhaven41ter dankzij vier vennoten, met een sterke visie rond veiligheid en comfort voor truckchauffeurs. Anno 2020 zijn het de gebroeders Vandel die deze visie verder zetten. Transport is dan ook onmisbaar in onze huidige maatschappij. De gebroeders Vandel, zelf ook actief in de transportwereld, weten waar de pijnpunten liggen in de sector. Daarom streven zij met Roadhaven41ter een oplossing te bieden op de problematiek rond veiligheid, comfort, hygiëne, parking en degelijke gezonde maaltijden. Dit doen ze door: verschillende beveiligingssystemen te gebruiken, verder bieden ze een restaurant, een Kelmo Mart en een aantal individuele, ruime douchecabines.</p>
  <div class="btn" style="left:608px;top:410px;width:145px;height:52px">Bekijk onze tijdlijn</div>
</section>

<section class="section meet">
  <h2 class="abs head center-title" style="top:105px">Vergaderen bij <span class="accent">Roadhaven 41Ter</span></h2>
  <p class="abs meet-text">Zoekt u nog een vergaderzaal? Dan is Roadhaven41ter de perfecte locatie. Wij beschikken over 4 vergaderruimte's met een maximum capaciteit van 70p. Beamer, wifi, whiteboard is allemaal aanwezig. Wij verzorgen een volledig drankenpakket met alle soorten frisdranken, waters &amp; koffie. Ook tijdens de lunchpauze bieden wij u verschillende pakketten aan, een broodje of een tas soep of zelfs een volledige menu!</p>
  <p class="abs" style="left:0;width:1200px;top:318px;font-size:15px">Indien u hier interesse in heeft kan u altijd bellen naar :</p>
  <div class="btn" style="left:528px;top:376px;width:144px;height:53px">+ 32 10 555 014</div>
</section>

<section class="section services">
  <h2 class="abs head center-title" style="top:34px">Onze <span class="accent">diensten</span></h2>
  <div class="service" style="left:73px"><div class="ring" role="img" aria-label="Roadhaven building exterior" style="background:#9fb4c6"></div>Kelmo Mart</div>
  <div class="service" style="left:298px"><div class="ring" role="img" aria-label="Sandwich bar counter" style="background:#c8a67c"></div>Broodjeskraam</div>
  <div class="service" style="left:507px"><div class="ring" role="img" aria-label="Restaurant dish being served" style="background:#6a5a4a"></div>Restaurant</div>
  <div class="service" style="left:717px"><div class="ring" role="img" aria-label="Secured parking lot with cars" style="background:#aab3bb"></div>Parkeermogelijkheden</div>
  <div class="service" style="left:926px"><div class="ring" role="img" aria-label="Meeting room with a person at a desk" style="background:#b9c3cf"></div>Vergaderzalen</div>
</section>

<section class="section resto">
  <div class="photo" role="img" aria-label="Man using a self-service coffee machine" style="left:175px;top:80px;width:398px;height:383px;background:linear-gradient(135deg,#7a7a72,#c8c2b6 60%,#4c4f4e)"></div>
  <p class="abs small-copy" style="left:173px;top:495px;width:405px">Elke zon- en feestdagen voorziet Roadhaven een uitgebreid ontbijtbuffet. Dit buffet is voorzien van: fruitsap, koffie, thee, water, broodjes, spek, eitjes, zalm, worstjes, kaas, chocoladebroodjes, muffins etc. We serveren het buffet van 8u-11u. Grotere groepen zijn ook welkom! We werken met dagverse producten dus het gamma kan variëren.</p>
  <div class="btn" style="left:173px;top:626px;width:114px;height:52px">Dagelijks</div>
  <div class="btn btn-outline" style="left:308px;top:626px;width:99px;height:52px">Menu</div>
  <h2 class="abs head" style="left:624px;top:82px;font-size:22px">Restaurant</h2>
  <p class="abs small-copy" style="left:624px;top:125px;width:405px">Ons restaurant is een gezellige warme plek om te vertoeven. Met onze uitgebreide menukaart is er voor ieder wat wils. Elke dag staat ons team klaar tot 22u om voor u een gezonde evenwichtige maaltijd te bereiden. In het restaurant is een ook voor de kleinste onder ons een fijne kinderhoek ingedeeld, en met mooi weer staat er op ons terras een springkasteel. Of u nu komt voor een uitgebreid diner of een snelle hap, bij Roadhaven bent u aan het juiste adres.</p>
  <div class="photo" role="img" aria-label="Fried squid rings with dip sauces on a wooden board" style="left:624px;top:303px;width:400px;height:380px;background:linear-gradient(150deg,#e9e4dc,#c98a4a 55%,#6f7a3a)"></div>
</section>

<section class="section blog">
  <h2 class="abs head center-title" style="top:102px">Laatste <span class="accent">blog</span></h2>
  <article class="post" style="left:96px">
    <div class="img" role="img" aria-label="Row of canned drinks" style="background:linear-gradient(180deg,#f3f0ec,#d8b9b4)"></div>
    <span class="date">15 June,2023</span>
    <h3>Sed ut perspiciatis unde omnis iste natus error sit voluptatem</h3>
    <p>Lorem ipsum dolor sit amet, consectetur adipiscing elit, sed do eiusmod tempor</p>
    <div class="more">LEES VERDER</div>
  </article>
  <article class="post" style="left:437px">
    <div class="img" role="img" aria-label="Grilled dish on a blue plate" style="background:linear-gradient(180deg,#d9dcd8,#c8883c 55%,#2d5c6a)"></div>
    <span class="date">15 June,2023</span>
    <h3>Sed ut perspiciatis unde omnis iste natus error sit voluptatem</h3>
    <p>Lorem ipsum dolor sit amet, consectetur adipiscing elit, sed do eiusmod tempor</p>
    <div class="more">LEES VERDER</div>
  </article>
  <article class="post" style="left:777px">
    <div class="img" role="img" aria-label="Shopper in a supermarket aisle" style="background:linear-gradient(90deg,#8a6b6b,#c6b8b0 50%,#6f5458)"></div>
    <span class="date">15 June,2023</span>
    <h3>Sed ut perspiciatis unde omnis iste natus error sit voluptatem</h3>
    <p>Lorem ipsum dolor sit amet, consectetur adipiscing elit, sed do eiusmod tempor</p>
    <div class="more">LEES VERDER</div>
  </article>
</section>

<section class="section contact">
  <h2 class="abs head center-title" style="top:74px;color:#fff;font-size:30px">Neem contact met ons op</h2>
  <div class="field" style="left:120px;top:158px;width:470px">First Name
    <svg width="14" height="14" viewBox="0 0 14 14"><circle cx="7" cy="4" r="3" fill="#777"/><path d="M1 14c0-4 3-6 6-6s6 2 6 6z" fill="#777"/></svg></div>
  <div class="field" style="left:605px;top:158px;width:474px">Last Name
    <svg width="14" height="14" viewBox="0 0 14 14"><circle cx="7" cy="4" r="3" fill="#777"/><path d="M1 14c0-4 3-6 6-6s6 2 6 6z" fill="#777"/></svg></div>
  <div class="field" style="left:120px;top:221px;width:470px">Email Address
    <svg width="15" height="12" viewBox="0 0 15 12"><rect width="15" height="12" rx="1" fill="#777"/><path d="M1 1l6.5 5L14 1" stroke="#fff" fill="none"/></svg></div>
  <div class="field" style="left:605px;top:221px;width:474px">Phone No
    <svg width="14" height="14" viewBox="0 0 14 14"><path d="M3 1l2 3-1.5 1.5c1 2 2.5 3.5 4.5 4.5L9.5 8.5l3 2-1 2.5C6 13 1 8 1 2z" fill="#777"/></svg></div>
  <div class="field" style="left:120px;top:283px;width:959px;height:96px;align-items:flex-start;padding-top:16px">Message
    <svg width="15" height="13" viewBox="0 0 15 13"><ellipse cx="7.5" cy="6" rx="6.5" ry="5" fill="none" stroke="#777" stroke-width="1.5"/></svg></div>
  <div class="btn" style="left:532px;top:462px;width:136px;height:46px;border-radius:23px;font-size:12px">Submit Now</div>
</section>

<footer class="section footer">
  <div class="abs" style="left:100px;top:165px;width:280px;font-family:'Oswald',sans-serif;font-weight:600;font-size:38px;color:var(--navy);line-height:1">ROADHAVEN 41TER</div>
  <div class="abs foot-title" style="left:472px;top:105px">Contact</div>
  <div class="contact-item" style="top:163px"><span class="icon-dot"><svg width="14" height="18" viewBox="0 0 14 18"><path d="M7 0a7 7 0 017 7c0 5-7 11-7 11S0 12 0 7a7 7 0 017-7z" fill="#fff"/><circle cx="7" cy="7" r="2.5" fill="#24235a"/></svg></span><div>Havenlaan 88<br>3590 Dorpveld</div></div>
  <div class="contact-item" style="top:235px"><span class="icon-dot"><svg width="16" height="16" viewBox="0 0 14 14"><path d="M3 1l2 3-1.5 1.5c1 2 2.5 3.5 4.5 4.5L9.5 8.5l3 2-1 2.5C6 13 1 8 1 2z" fill="#fff"/></svg></span><div><b style="font-weight:500">Restaurant</b><br>010 555 872</div></div>
  <div class="contact-item" style="top:305px"><span class="icon-dot"><svg width="16" height="12" viewBox="0 0 15 12"><rect width="15" height="12" rx="1" fill="#fff"/><path d="M1 1l6.5 5L14 1" stroke="#24235a" fill="none"/></svg></span><div><b style="font-weight:500">E-mail</b><br>jobs@calmroadhaven.eu</div></div>
  <div class="abs" style="left:763px;top:105px"><div class="foot-title">Snelle links</div>
    <div class="foot-list">Home<br>Over ons<br>Broodjesbar<br>Restaurant<br>Parking<br>Kelmo Mart<br>Contact</div></div>
  <div class="abs" style="left:968px;top:105px"><div class="foot-title">Steun</div>
    <div class="foot-list">algemene<br>voorwaarden<br>Privacybeleid<br>Over ons<br>Steun</div></div>
  <div class="abs" style="left:0;width:1200px;top:400px;text-align:center;font-size:13px;color:#333">©Copyrights 2023 Calmroadhaven &nbsp;|&nbsp; All Rights Reserved</div>
</footer>

</body>
</html>
```